Book Cover for Fitness Trainer for Men

My name is Mabel Joy Crane. I am a female Fitness Trainer for Men.
I need a new Book Cover Design for my second book and a back of the book.
Both with updated text.
#A… Book Cover… I like the bright red and yellow colors.
I like the weight rack and the bold headline Font
#B… Book Cover…I like the full frontal sexier body. I don not like the font style.
I want the new design sexier; super sexy. Even more eye catching for guys.
I want to push the envelope to the point of almost too much sexy.
An Brindlo book 6”x9”, 150 pages

Target Market(s)

Men

Industry/Entity Type

Health and fitness for men

Colors
FFF300
FFF600
FEFA6F
FFFEC7
FFFEE8
EB3D1F
EC4F4E
F09395
F8D3D4
FCEDEE

Requirements
Must have
• Sexy & eye catching.

```html
<!DOCTYPE html>
<html lang="en">
<head>
<meta charset="utf-8">
<title>Mabel Joy Crane – Fitness Trainer for Men, Volume II</title>
<link href="https://fonts.googleapis.com/css2?family=Open+Sans:ital,wght@0,400;0,600;0,700;0,800;1,400;1,600;1,700;1,800&display=swap" rel="stylesheet">
<style>
  :root {
    --red: #eb3d1f;
    --red-soft: #ec4f4e;
    --pink: #f09395;
    --yellow: #fff300;
    --yellow-pale: #fefa6f;
    --ink: #111111;
    --charcoal: #2e2e2e;
    --white: #ffffff;
    --back-dark: #1c0c0a;
    --back-mid: #3a1410;
  }
  * { box-sizing: border-box; margin: 0; padding: 0; }
  html, body { width: 1200px; height: 881px; overflow: hidden; background: #ffffff; }
  body { font-family: "Open Sans", Arial, sans-serif; }

  .cover-spread { position: relative; width: 1200px; height: 881px; }

  /* ---------- Back cover ---------- */
  .back-cover {
    position: absolute; left: 0; top: 0; width: 584px; height: 881px;
    background: linear-gradient(100deg, var(--back-mid) 0%, #2a0f0c 40%, var(--back-dark) 75%, #140807 100%);
    color: var(--white); font-style: italic;
  }
  .back-photo {
    position: absolute; left: 180px; top: 0; width: 404px; height: 881px;
    background: radial-gradient(ellipse at 55% 40%, rgba(150,90,70,0.35) 0%, rgba(80,35,25,0.2) 45%, rgba(0,0,0,0) 75%);
  }
  .back-copy {
    position: absolute; left: 46px; top: 52px; width: 518px;
    font-size: 11.6px; line-height: 1.42; font-weight: 600;
  }
  .back-copy p { margin-bottom: 17px; }
  .back-copy .small { font-weight: 400; }
  .back-headline {
    position: absolute; left: 0; top: 384px; width: 584px; text-align: center;
    color: var(--red); font-size: 21px; font-weight: 700;
  }
  .testimonials {
    position: absolute; left: 46px; top: 424px; width: 518px;
    font-size: 10.6px; line-height: 1.45; font-weight: 600;
  }
  .testimonials p { margin-bottom: 12px; }
  .author-photo {
    position: absolute; left: 46px; top: 677px; width: 100px; height: 118px;
    border: 2px solid #c9a58a;
    background: linear-gradient(160deg, #e7c39a 0%, #c48a62 55%, #4c6a5c 100%);
  }
  .author-note {
    position: absolute; left: 153px; top: 686px; width: 410px;
    font-size: 11px; line-height: 1.45; font-weight: 600;
  }
  .author-note .accent { color: var(--red); }
  .author-sign { position: absolute; left: 153px; top: 762px; font-size: 12px; line-height: 1.35; color: var(--pink); }
  .author-sign .name { font-weight: 600; }
  .author-sign .role { font-size: 10.5px; }
  .back-tagline {
    position: absolute; left: 46px; top: 822px; color: var(--red);
    font-size: 14.2px; font-weight: 600;
  }

  /* ---------- Spine ---------- */
  .spine {
    position: absolute; left: 584px; top: 0; width: 31px; height: 881px;
    background: #1a0a08;
  }
  .spine-title {
    position: absolute; left: 50%; top: 320px; transform: translateX(-50%) rotate(90deg);
    transform-origin: center; white-space: nowrap; font-style: italic; font-size: 13px;
    width: 0; display: flex; justify-content: center;
  }
  .spine-title span { display: inline-block; }
  .spine-title .spine-name { color: var(--red); font-weight: 700; margin-right: 14px; }
  .spine-title .spine-sub { color: var(--white); font-weight: 400; font-size: 11.5px; }

  /* ---------- Front cover ---------- */
  .front-cover { position: absolute; left: 615px; top: 0; width: 585px; height: 881px; background: var(--white); overflow: hidden; }
  .front-art { position: absolute; inset: 0; width: 585px; height: 881px; }
  .author-name {
    position: absolute; left: 26px; top: 96px; font-size: 37px; font-weight: 800; font-style: italic;
    color: var(--yellow); text-shadow: 2px 2px 0 #2b2b2b; letter-spacing: -0.5px;
  }
  .author-role {
    position: absolute; left: 28px; top: 150px; font-size: 29px; line-height: 1.05;
    font-weight: 700; font-style: italic; color: var(--charcoal);
  }
  .front-hook {
    position: absolute; left: 26px; top: 640px; font-size: 23px; line-height: 1.2;
    font-weight: 800; font-style: italic; color: var(--red);
    text-shadow: 1.5px 1.5px 0 var(--yellow), -1px -1px 0 var(--yellow);
  }
  .front-hook .line2 { display: block; padding-left: 13px; }
  .front-promise {
    position: absolute; left: 70px; top: 728px; font-size: 20px; line-height: 1.3;
    font-weight: 700; font-style: italic; color: var(--ink);
  }
  .front-promise span { display: block; }
  .front-promise .l2 { padding-left: 72px; }
  .front-promise .l3 { padding-left: 108px; }
  .volume-label {
    position: absolute; left: 472px; top: 803px; font-size: 14px; font-weight: 800;
    font-style: italic; color: var(--yellow);
  }
</style>
</head>
<body>
<main class="cover-spread">

  <section class="back-cover">
    <div class="back-photo" role="img" aria-label="Dim, warm-toned photograph of a trainer's body in the background"></div>

    <div class="back-copy">
      <p>I've been using eye candy to get guys interested in health and fitness since the day I walked in the gym and turned heads. I figured if you wanted Tits &amp;Ass I'd give it to you. Enough to make a buck and get my guys healthier. As a personal fitness trainer for Men I've learned…that not all Guys are the same. Each of you is different and You need to find what works for You. When you do… the the pounds melt away, your gut shrinks, and your health improves.</p>
      <p>You'll love the new you. Your girlfriend will love it. Your wife will love it. Nothing a woman loves more than a long rock hard man in shape.</p>
      <p class="small">While everybody in the fitness community screams and yells about gym memberships, 30day challenges, and complete diet changes … My Guys don't do all that. My Guys are Real Men with Real bodies. Real Men that work for a living and don't have time to live in the gym.</p>
      <p class="small">Real men are tired of gym rats with "Look at me" egos, God given 1% body fat and abs you'll never get. These guys are full of Shit! And they're the first one to buy my book. Yagotta love it.</p>
    </div>

    <h2 class="back-headline">You need to find what works for you.</h2>

    <div class="testimonials">
      <p>"I made a few adjustment in my meals added a minimum amount of exercise and lost 17 pounds in three months. Thanks Mabel. Couldn't have done it without you.".</p>
      <p>"Mabel I took your bait and it actually made sense. Can't believe you got me exercising. My gut shrunk and had to buy new pants. Best 20 bucks I ever spent."“I've tried a few expensive 30day programs but your Ultimate Workout was all I ever needed. You're right No F**king secret here."“Strategically eating Fast food is genius. Never thought I could still eat "the good stuff" and lose weight. WOW!"“My increasing weight was scaring the hell out of me. Showing me that it's the little changes I can do…that has changed everything."“Everybody wanted me to make big drastic changes in my life. I can't do that. All these little "Tricks of the Trade" I can do."<br>Thank you Mabel."</p>
    </div>

    <div class="author-photo" role="img" aria-label="Author portrait of Mabel Joy Crane"></div>
    <p class="author-note"><span class="accent">Real Men can be fit, healthy and in shape no matter their size, weight, or body fat.</span> My mission is to get your lazy ass in shape by finding what works for you. If I need to get your attention first…Then that's what I'll do.</p>
    <div class="author-sign">
      <div class="name">Mabel Joy Crane</div>
      <div class="role">Fitness Trainer for Men</div>
    </div>
    <p class="back-tagline">Think you can do Twenty bucks to Get You Hot, Sweaty, and Hard?</p>
  </section>

  <aside class="spine">
    <div class="spine-title"><span class="spine-name">Mabel Joy Crane</span><span class="spine-sub">Fitness Trainer for Men</span></div>
  </aside>

  <section class="front-cover">
    <svg class="front-art" viewBox="0 0 442 666" preserveAspectRatio="none" aria-hidden="false">
      <defs>
        <linearGradient id="gym-photo" x1="0" y1="0" x2="1" y2="1">
          <stop offset="0" stop-color="#3a3a3a"/>
          <stop offset="0.45" stop-color="#1b1b1b"/>
          <stop offset="0.7" stop-color="#7a2a22"/>
          <stop offset="1" stop-color="#111111"/>
        </linearGradient>
      </defs>
      <polygon class="band-red" points="0,0 340,0 0,460" fill="#eb3d1f"/>
      <polygon class="band-white-stripe" points="305,0 315,0 120,264 113,255" fill="#ffffff" opacity="0.9"/>
      <polygon class="band-dark-stripe" points="352,0 370,0 0,500 0,476" fill="#2b2b2b"/>
      <polygon class="panel-black" points="380,0 442,0 442,666 380,666 115,440 60,420" fill="#111111"/>
      <g role="img" aria-label="Photograph of a woman in black sportswear lifting a dumbbell beside a red weight bench in a gym">
        <polygon points="398,0 442,0 442,565 140,420 88,410" fill="url(#gym-photo)"/>
      </g>
    </svg>

    <h1 class="author-name">Mabel Joy Crane</h1>
    <p class="author-role">Fitness Trainer<br>for Men</p>

    <p class="front-hook">Helping Guys Get<span class="line2">Hot, Sweaty, &amp; Hard</span></p>
    <p class="front-promise">
      <span class="l1">so Pounds Melt Away,</span>
      <span class="l2">Your Gut Shrinks,</span>
      <span class="l3">&amp; You Last Longer.</span>
    </p>
    <p class="volume-label">Volume II</p>
  </section>

</main>
</body>
</html>
```